Business Card Design
Brightvale Marks
Modern
Kemi Varo
47 Olumide Bankole Crescent
Wuse 2
Abuja
Nigeria
info@brightvalemarks.com
www.brightvalemarks.com

```html
<!DOCTYPE html>
<html lang="en">
<head>
<meta charset="utf-8">
<title>Brightvale Marks – Business Card</title>
<link href="https://fonts.googleapis.com/css2?family=Cinzel:wght@400;600&family=Open+Sans:wght@400;600&display=swap" rel="stylesheet">
<style>
  :root {
    --page: #e9e6e2;
    --card: #0b0b0c;
    --card-edge: #1a1a1c;
    --brand-blue: #3a8fd0;
    --brand-green: #8cc63f;
    --text-light: #e6e6e6;
    --text-muted: #9a9a9a;
  }
  * { margin: 0; padding: 0; box-sizing: border-box; }
  html, body { width: 1200px; height: 646px; overflow: hidden; background: var(--page); }
  .canvas { position: relative; width: 1200px; height: 646px; }
  .card {
    position: absolute; top: 168px; width: 540px; height: 310px;
    background: radial-gradient(ellipse at 40% 30%, var(--card-edge), var(--card) 70%);
    box-shadow: 0 8px 22px rgba(0,0,0,.35);
    overflow: hidden;
  }
  .card--front { left: 40px; }
  .card--back { left: 620px; }

  .brand { position: absolute; left: 34px; top: 40px; display: flex; align-items: center; gap: 12px; }
  .brand__dot { width: 18px; height: 18px; border-radius: 50%; background: var(--brand-green); }
  .brand__name {
    font-family: 'Cinzel', serif; font-weight: 400; font-size: 21px;
    color: var(--brand-blue); letter-spacing: .5px; text-transform: uppercase;
  }
  .tagline {
    position: absolute; left: 34px; top: 74px;
    font-family: 'Cinzel', serif; font-size: 7px; letter-spacing: .6px;
    color: var(--text-muted); text-transform: uppercase;
  }
  .person {
    position: absolute; left: 34px; top: 116px;
    font-family: 'Cinzel', serif; font-size: 18px; color: var(--brand-green);
  }
  .contacts {
    position: absolute; left: 34px; top: 156px; list-style: none;
    font-family: 'Open Sans', sans-serif; font-size: 11px; color: var(--text-light);
  }
  .contacts li { display: flex; align-items: center; gap: 7px; height: 22px; }
  .contacts svg { width: 10px; height: 10px; fill: var(--text-light); flex: none; }
  .front-mark {
    position: absolute; right: 46px; top: 66px; width: 120px; height: 120px;
    border-radius: 50%; background: var(--brand-blue); opacity: .9;
  }

  .back-brand {
    position: absolute; left: 0; right: 0; top: 110px;
    display: flex; justify-content: center; align-items: center; gap: 12px;
  }
  .url {
    position: absolute; right: 40px; bottom: 36px;
    font-family: 'Cinzel', serif; font-size: 15px; letter-spacing: 2px; color: var(--text-light);
  }
</style>
</head>
<body>
<main class="canvas">
  <section class="card card--front" aria-label="Business card front">
    <div class="brand">
      <span class="brand__dot"></span>
      <span class="brand__name">Brightvale Marks</span>
    </div>
    <p class="tagline">Brand marks made bright</p>
    <p class="person">Kemi Varo</p>
    <ul class="contacts">
      <li><svg viewBox="0 0 10 10"><path d="M2 0h2l1 3-1.5 1a6 6 0 0 0 2.5 2.5L7 5l3 1v2c0 1-1 2-2 2A8 8 0 0 1 0 2c0-1 1-2 2-2z"/></svg>08120004517</li>
      <li><svg viewBox="0 0 10 10"><path d="M0 2h10v6H0zM0 2l5 3.5L10 2" stroke="#0b0b0c" stroke-width=".8"/></svg>info@brightvalemarks.com</li>
      <li><svg viewBox="0 0 10 10"><path d="M5 0l5 4.5H8.5V10h-7V4.5H0z"/></svg>47 Olumide Bankole Crescent, Wuse 2, Abuja,Nigeria</li>
    </ul>
    <div class="front-mark"></div>
  </section>

  <section class="card card--back" aria-label="Business card back">
    <div class="back-brand">
      <span class="brand__dot"></span>
      <span class="brand__name">Brightvale Marks</span>
    </div>
    <p class="url">www.brightvalemarks.com</p>
  </section>
</main>
</body>
</html>
```